Company Website

We need an interactive website designed that for new company. Our company is in the Automotive fleet maintenance business. We have wide ranging customers in many industries e.g Aviation industry, construction industry, transportation etc.
We would like the website to have login accounts where customers can register, login and access their service history. Also we would like to have an appointment system where customers could schedule appointments, once appointments are made that time would no longer be available to be selected as it would be booked etc.

The website should also be updatable and provide areas for showcasing
Our services
Products/parts (possibly store front)
Customer feedback
Appointments
Our customers (where our customers can advertise or be showcased)
About us
Contacts
gallery

We would like designs that have a modern, corporate feel, One that is user friendly.
prefer a design that does not look like a template.

Target Market(s)

Medium to large companies, small business owners and the general motoring public.

Industry/Entity Type

Construction

Requirements
Must have
• Customer login set up so a database of customer vehicle maintenance history as well as the ability to schedule repairs via their account. They could also check the status of a repair.
Nice to have
• Photo gallery to show case current projects.
Our customers page where we can show case our clients they could also post their events on there, promotions etc.

The theme Should be something that's reflective of our core business; fleet maintenance. It would be nice to capture some sort of background in there that depicts some of that for example mixer trucks, tractors,loaders excavators forklifts cars trucks. That's what we deal with. It's up to the designer to capture the Essence of this as much as possible. Impress me.
Should not have
• Would prefer a custom website not a template.

```html
<!DOCTYPE html>
<html lang="en">
<head>
<meta charset="utf-8">
<title>Meridian Fleet &amp; Auto Maintenance</title>
<link rel="stylesheet" href="https://fonts.googleapis.com/css2?family=Mulish:wght@400;700;800&family=Questrial&display=swap">
<style>
  :root {
    --red: #b5121b;
    --red-dark: #9e1118;
    --yellow: #f3c400;
    --ink: #1f1f1f;
    --text: #333333;
    --field: #d9d9d9;
    --footer: #222222;
    --footer-base: #151212;
    --footer-link: #d6d6d6;
    --footer-nav: #a9a9a9;
    --white: #ffffff;
  }
  * { margin: 0; padding: 0; box-sizing: border-box; }
  html, body { width: 833px; height: 1200px; overflow: hidden; background: var(--white); }
  body { position: relative; font-family: "Mulish", sans-serif; color: var(--text); }
  .abs { position: absolute; }

  /* Header */
  .brand { left: 30px; top: 42px; color: var(--red); font-weight: 800; }
  .brand-name { font-size: 34px; letter-spacing: 3px; line-height: 1; }
  .brand-tag { font-size: 12.5px; margin-top: 6px; letter-spacing: 0.2px; }
  .login-field { left: 635px; width: 85px; height: 18px; background: var(--field); color: #8a8a8a;
    font-size: 9px; text-align: center; line-height: 18px; }
  .login-user { top: 51px; }
  .login-pass { top: 73px; }
  .login-go { left: 720px; top: 73px; width: 18px; height: 18px; background: var(--red); }
  .rule-top { left: 0; top: 112px; width: 833px; height: 8px; background: var(--red); }
  .notch { left: 664px; top: 100px; }

  /* Navigation */
  .main-nav { left: 0; top: 120px; width: 833px; height: 38px; }
  .main-nav a { position: absolute; top: 12px; transform: translateX(-50%); font-size: 11.5px;
    color: var(--ink); text-decoration: none; }

  /* Hero */
  .hero { left: 0; top: 158px; width: 833px; height: 289px; background: var(--red); }
  .hero-title { left: 36px; top: 191px; font-size: 28px; font-weight: 800; color: var(--white); }
  .hero-copy { left: 35px; top: 238px; width: 345px; font-family: "Questrial", sans-serif;
    font-size: 16px; line-height: 25px; color: var(--white); }
  .hero-btn { left: 35px; top: 331px; width: 145px; height: 41px; background: var(--yellow);
    color: var(--ink); font-weight: 800; font-size: 16px; letter-spacing: 1px; text-align: center; line-height: 41px; }
  .hero-photo { left: 445px; top: 178px; width: 355px; height: 259px; border-radius: 4px;
    background: linear-gradient(135deg, #8a1a1e 0%, #3a3a3a 40%, #d6b326 75%, #a3141b 100%); }
  .rule-hero { left: 0; top: 454px; width: 833px; height: 6px; background: var(--red); }

  /* News columns */
  .news-date { top: 482px; width: 262px; text-align: center; font-family: "Questrial", sans-serif;
    font-size: 20.5px; font-weight: 400; color: var(--red); }
  .news-photo { border-radius: 3px; }
  .photo-red { background: linear-gradient(160deg, #f1f1f1 0%, #444 45%, #d42a2a 75%, #f3f3f3 100%); }
  .photo-yellow { background: linear-gradient(160deg, #f3f3f3 0%, #2d2d2d 40%, #e1bd1f 70%, #f3f3f3 100%); }
  .photo-orange { background: linear-gradient(160deg, #f3f3f3 0%, #2a3e8c 40%, #f08a1a 72%, #f3f3f3 100%); }
  .news-copy { top: 710px; width: 246px; font-family: "Questrial", sans-serif; font-size: 10.4px;
    line-height: 12.6px; color: var(--text); }
  .read-more { top: 868px; width: 94px; height: 28px; border-radius: 6px; background: var(--red);
    color: var(--white); font-size: 10px; text-align: center; line-height: 28px; }

  /* Archive footer */
  .archive { left: 0; top: 926px; width: 833px; height: 223px; background: var(--footer); }
  .archive-col { top: 960px; }
  .archive-col h3 { font-family: "Questrial", sans-serif; font-weight: 400; font-size: 20.5px;
    color: var(--red); margin-bottom: 17px; }
  .archive-col a { display: block; font-family: "Questrial", sans-serif; font-size: 10.5px;
    color: var(--footer-link); text-decoration: none; line-height: 23.7px; }

  /* Base bar */
  .base { left: 0; top: 1149px; width: 833px; height: 51px; background: var(--footer-base); }
  .base-brand { left: 43px; top: 1162px; color: var(--red); font-weight: 800; }
  .base-brand .brand-name { font-size: 15px; letter-spacing: 1.5px; }
  .base-brand .brand-tag { font-size: 6.5px; margin-top: 3px; }
  .base-nav a { position: absolute; top: 1168px; font-size: 10.5px; color: var(--footer-nav); text-decoration: none; }
  .social { top: 1160px; width: 26px; height: 26px; background: var(--red); }
</style>
</head>
<body>

<header>
  <div class="abs brand">
    <div class="brand-name">MERIDIAN</div>
    <div class="brand-tag">FLEET &amp; AUTO MAINTENANCE</div>
  </div>
  <div class="abs login-field login-user">USER</div>
  <div class="abs login-field login-pass">PASS</div>
  <div class="abs login-go" aria-label="Sign in"></div>
  <svg class="abs notch" width="28" height="14" viewBox="0 0 28 14"><polygon points="0,14 14,0 28,14" fill="#b5121b"/></svg>
  <div class="abs rule-top"></div>
  <nav class="abs main-nav">
    <a style="left:163px">ABOUT</a>
    <a style="left:252px">SERVICES</a>
    <a style="left:350px">PRODUCTS</a>
    <a style="left:447px">GALLERY</a>
    <a style="left:556px">APPOINTMENTS</a>
    <a style="left:664px">CONTACT</a>
  </nav>
</header>

<section>
  <div class="abs hero"></div>
  <h1 class="abs hero-title">Lorem ipsum dolor site amet</h1>
  <p class="abs hero-copy">und consectetur adipiscing elit, quid amet et neae lorem sit quid et und consectetur dolor sit elit.</p>
  <div class="abs hero-btn">VIEW MORE</div>
  <div class="abs hero-photo" role="img" aria-label="Yellow forklift carrying a loaded pallet"></div>
  <div class="abs rule-hero"></div>
</section>

<section>
  <h2 class="abs news-date" style="left:25px">December 2013</h2>
  <h2 class="abs news-date" style="left:287px">November 2013</h2>
  <h2 class="abs news-date" style="left:548px">November 2013</h2>

  <div class="abs news-photo photo-red" style="left:20px; top:522px; width:235px; height:176px" role="img" aria-label="Red electric forklift"></div>
  <div class="abs news-photo photo-yellow" style="left:300px; top:527px; width:235px; height:145px" role="img" aria-label="Yellow forklift with pallet"></div>
  <div class="abs news-photo photo-orange" style="left:563px; top:508px; width:199px; height:197px" role="img" aria-label="Orange forklift with blue mast"></div>

  <p class="abs news-copy" style="left:32px">Lorem ipsum dolor site amet und consectetur adipiscing elit, quid amet et neae lorem sit quid et und consectetur dolor sit elit.&nbsp; Lorem ipsum, dolor sit amet consectetur adipiscing elit sit amet dolor.&nbsp; Lorem ipsum dolor site amet und consectetur adipiscing elit, quid amet et neae lorem sit quid adipiscing elit sit amet dolor. Lorem ipsum dolor site amet und consectetur adipiscing elit, quid amet et neae lorem sit quid et und consectetur dolor sit elit.</p>
  <p class="abs news-copy" style="left:293px">Lorem ipsum dolor site amet und consectetur adipiscing elit, quid amet et neae lorem sit quid et und consectetur dolor sit elit.&nbsp; Lorem ipsum, dolor sit amet consectetur adipiscing elit sit amet dolor.&nbsp; Lorem ipsum dolor site amet und consectetur adipiscing elit, quid amet et neae lorem sit quid et und consectetur dolor sit elit. Lorem ipsum, dolor sit amet consectetur adipiscing elit sit amet dolor.</p>
  <p class="abs news-copy" style="left:555px">Lorem ipsum dolor site amet und consectetur adipiscing elit, quid amet et neae lorem sit quid et und consectetur dolor sit elit.&nbsp; Lorem ipsum, dolor sit amet consectetur adipiscing elit sit amet dolor.&nbsp; Lorem ipsum dolor site amet und consectetur adipiscing elit, quid amet et neae lorem sit quid et und consectetur dolor sit elit. Lorem ipsum, dolor sit amet consectetur adipiscing elit sit amet dolor.&nbsp; Lorem ipsum dolor site amet.</p>

  <div class="abs read-more" style="left:187px">READ MORE</div>
  <div class="abs read-more" style="left:446px">READ MORE</div>
  <div class="abs read-more" style="left:711px">READ MORE</div>
</section>

<footer>
  <div class="abs archive"></div>
  <div class="abs archive-col" style="left:129px">
    <h3>December</h3>
    <a>link one goes here</a><a>link two goes here</a><a>link one goes here</a><a>link two goes here</a>
  </div>
  <div class="abs archive-col" style="left:287px">
    <h3>November</h3>
    <a>link one goes here</a><a>link one goes here</a><a>link one goes here</a><a>link one goes here</a>
  </div>
  <div class="abs archive-col" style="left:445px">
    <h3>October</h3>
    <a>link one goes here</a><a>link two goes here</a><a>link one goes here</a><a>link two goes here</a>
  </div>
  <div class="abs archive-col" style="left:595px">
    <h3>September</h3>
    <a>link one goes here</a><a>link two goes here</a><a>link one goes here</a><a>link two goes here</a>
  </div>

  <div class="abs base"></div>
  <div class="abs base-brand">
    <div class="brand-name">MERIDIAN</div>
    <div class="brand-tag">FLEET &amp; AUTO MAINTENANCE</div>
  </div>
  <nav class="base-nav">
    <a style="left:228px">ABOUT</a>
    <a style="left:285px">SERVICES</a>
    <a style="left:356px">PRODUCTS</a>
    <a style="left:433px">GALLERY</a>
    <a style="left:501px">APPOINTMENTS</a>
    <a style="left:602px">CONTACT</a>
  </nav>
  <div class="abs social" style="left:712px" aria-label="Social link"></div>
  <div class="abs social" style="left:748px" aria-label="Social link"></div>
  <div class="abs social" style="left:782px" aria-label="Social link"></div>
</footer>

</body>
</html>
```